Create branded design templates/backgrounds for social media based on UK property investing company

I'd like Instagram, Facebook and Linkedin backgrounds/templates to add text to, based on my logo design and business of UK holiday let investing. Ideally I'd have some base designs for me to approve, then engage with the winning designer further to create about 50 different templates. I looking for a mixture of templates with the logo and using logo colours, others of internal holiday let photos including logos and a few of my photo imposed on the front of them.
Updates

Slow in providing feedback

Target Market(s)

Middle aged adults

Industry/Entity Type

Holiday let properties

Requirements
Must have
• a distinct brand look that can be replicated

```html
<!DOCTYPE html>
<html lang="en">
<head>
<meta charset="utf-8">
<title>Brightstay Homes – Holiday House Portfolio</title>
<link rel="stylesheet" href="https://fonts.googleapis.com/css2?family=Montserrat:wght@400;500;800;900&display=swap">
<style>
  :root{
    --blue:#0a86d3;
    --blue-dark:#0572bd;
    --yellow:#f8d42a;
    --green:#55a80b;
    --white:#ffffff;
    --ink:#2b2b2b;
    --brick-1:#8a3b24;
    --brick-2:#a6543a;
    --brick-3:#5e2a1c;
  }
  *{margin:0;padding:0;box-sizing:border-box}
  html,body{width:1200px;height:1200px;overflow:hidden;background:var(--white)}
  .poster{position:relative;width:1200px;height:1200px;overflow:hidden;font-family:"Montserrat",sans-serif;background:var(--white)}

  .photo{position:absolute;left:0;top:0;width:1200px;height:1000px;
    background:linear-gradient(160deg,#d9dfe3 0%,var(--brick-2) 18%,var(--brick-1) 45%,var(--brick-3) 62%,#6f6a5c 80%,#4f5447 100%)}

  .frame-line{position:absolute;left:0;top:0;width:1200px;height:1200px}

  .brand-card{position:absolute;left:32px;top:-2px;width:470px;height:160px;background:var(--white);
    border-radius:0 0 50px 50px;display:flex;align-items:center;padding-left:46px;gap:16px}
  .brand-card .mark{width:34px;height:34px;background:var(--blue)}
  .brand-card .name{font-weight:800;font-size:36px;color:var(--blue);letter-spacing:.5px}

  .green-band{position:absolute;left:0;top:219px;width:646px;height:60px;background:var(--green);border-top-right-radius:56px}
  .yellow-strip{position:absolute;left:620px;top:286px;width:94px;height:710px;background:var(--yellow);border-top-right-radius:56px}
  .blue-panel{position:absolute;left:0;top:251px;width:683px;height:829px;background:var(--blue);border-top-right-radius:56px}
  .yellow-base{position:absolute;left:0;top:1075px;width:480px;height:38px;background:var(--yellow)}

  .footer-shape{position:absolute;left:0;top:0;width:1200px;height:1200px}

  .tagline{position:absolute;left:83px;top:362px;font-size:38px;font-weight:400;color:var(--white)}
  .tagline b{font-weight:800;color:var(--yellow)}
  .headline{position:absolute;left:82px;top:440px;font-size:81px;font-weight:800;line-height:75px;color:var(--white);letter-spacing:-1px}
  .headline .accent{color:var(--yellow)}
  .lead{position:absolute;left:84px;top:855px;width:540px;font-size:30px;line-height:32px;font-weight:400;color:var(--white)}

  .cta{position:absolute;left:440px;top:1052px;width:216px;text-align:right;font-size:53px;font-weight:900;line-height:50px;color:var(--blue);letter-spacing:-1.5px}
  .icons{position:absolute;left:677px;top:1054px;width:44px}
  .icons svg{display:block}
  .contact{position:absolute;right:54px;top:1052px;text-align:right;color:var(--blue)}
  .contact .phone{font-size:53px;font-weight:900;letter-spacing:-1px;line-height:56px}
  .contact .email{font-size:31px;font-weight:500;line-height:42px;margin-top:4px}
</style>
</head>
<body>
<div class="poster">
  <div class="photo" role="img" aria-label="Photo of a smiling man in glasses in front of red-brick Victorian terraced houses with white bay windows"></div>

  <svg class="frame-line" viewBox="0 0 1200 1200" aria-hidden="true">
    <path d="M500 75 H1090 Q1114 75 1114 99 V996" fill="none" stroke="var(--yellow)" stroke-width="4"/>
    <path d="M85 158 V252" fill="none" stroke="var(--yellow)" stroke-width="4"/>
  </svg>

  <div class="brand-card">
    <span class="mark"></span>
    <span class="name">Brightstay Homes</span>
  </div>

  <div class="green-band"></div>
  <div class="yellow-strip"></div>
  <div class="blue-panel"></div>
  <div class="yellow-base"></div>

  <svg class="footer-shape" viewBox="0 0 1200 1200" aria-hidden="true">
    <path d="M0 1113 H408 C430 1040 480 996 560 996 H1200 V1200 H0 Z" fill="var(--white)"/>
    <path d="M88 1108 Q92 1126 112 1126 H405" fill="none" stroke="var(--yellow)" stroke-width="4"/>
  </svg>

  <p class="tagline">Invest In <b>YOUR</b> Future</p>
  <h1 class="headline">Choose &amp;<br>Invest in our<br><span class="accent">Holiday House<br>Portfolio</span> &amp;<br>Prosper.</h1>
  <p class="lead">Get in contact with us and we will advice, consult and create a perfectly tailored plan for you to invest and maximise your ROI.</p>

  <div class="cta">GET IN<br>TOUCH</div>
  <div class="icons" aria-hidden="true">
    <svg width="44" height="44" viewBox="0 0 24 24"><path fill="var(--green)" d="M6.6 10.8a15.1 15.1 0 0 0 6.6 6.6l2.2-2.2a1 1 0 0 1 1-.25 11.4 11.4 0 0 0 3.6.57 1 1 0 0 1 1 1V20a1 1 0 0 1-1 1A17 17 0 0 1 3 4a1 1 0 0 1 1-1h3.5a1 1 0 0 1 1 1c0 1.25.2 2.45.57 3.57a1 1 0 0 1-.25 1z"/></svg>
    <svg width="44" height="40" viewBox="0 0 44 34" style="margin-top:12px"><rect x="0" y="0" width="44" height="34" rx="3" fill="var(--green)"/><path d="M2 3 L22 19 L42 3" fill="none" stroke="var(--white)" stroke-width="3"/></svg>
  </div>
  <div class="contact">
    <div class="phone">+286 5120 408</div>
    <div class="email">info@brightstayhomes.uk</div>
  </div>
</div>
</body>
</html>
```